Letterhead Design

We need a new Letterhead design for a 30 year old Electrical Company. We service domestic and commercial places. We have a logo recently made so to incorporate that. Using same colours or interested to see others added.
Would like to see a couple of options with all the info in letterhead, then another with info in a footnote down the bottom.

info needed to be added:

-Lic. No 48162
8/22-24 Larkin Rd, Tolvern 2087
W - brightcoilpower.com.au
T - (02) 9471 3825
M - 0427 593 168
E - info@brightcoilpower.com.au
ABN: 42 597 214 630

Electrical

```html
<!DOCTYPE html>
<html lang="en">
<head>
<meta charset="utf-8">
<title>Brightcoil Power Letterhead</title>
<link href="https://fonts.googleapis.com/css2?family=Hind:wght@400;500;600&display=swap" rel="stylesheet">
<style>
  :root {
    --orange: #f47a36;
    --orange-light: #f8934a;
    --navy: #1b2a3a;
    --grey: #a9acaf;
    --paper: #ffffff;
    --backdrop: #d9dadc;
    --watermark: #eef1f3;
  }
  html, body { margin: 0; padding: 0; overflow: hidden; }
  body {
    width: 1000px; height: 1200px;
    background: var(--backdrop);
    font-family: "Hind", sans-serif;
    position: relative;
  }
  .letterhead {
    position: absolute; left: 90px; top: 20px;
    width: 820px; height: 1160px;
    background: var(--paper);
    box-shadow: 0 2px 14px rgba(0,0,0,.18);
    overflow: hidden;
  }
  .shapes { position: absolute; inset: 0; }
  .brand-name {
    position: absolute; left: 66px; top: 60px;
    font-size: 40px; font-weight: 600; color: var(--navy);
    line-height: 1; margin: 0;
  }
  .watermark-name {
    position: absolute; left: 0; right: 0; top: 500px;
    text-align: center;
    font-size: 96px; font-weight: 600; color: var(--watermark);
    line-height: 1;
  }
  .info { position: absolute; color: #fff; font-size: 17px; line-height: 1; display: flex; align-items: center; gap: 7px; white-space: nowrap; }
  .info svg { width: 16px; height: 16px; flex: none; }
  .licence { left: 432px; top: 75px; }
  .website { left: 566px; top: 75px; }
  .email { left: 546px; top: 1049px; }
  .address { left: 48px; top: 1096px; }
  .phone { left: 385px; top: 1096px; }
  .mobile { left: 532px; top: 1096px; }
  .abn { left: 708px; top: 1099px; font-size: 12px; font-weight: 600; }
</style>
</head>
<body>
<main class="letterhead">
  <svg class="shapes" viewBox="0 0 820 1160" aria-hidden="true">
    <!-- header -->
    <polygon points="660,40 745,40 735,56 650,56" fill="var(--grey)"/>
    <polygon points="745,40 820,40 820,60 732,60" fill="var(--navy)"/>
    <polygon points="377,60 820,60 820,106 410,106" fill="var(--orange)"/>
    <polygon points="520,60 820,60 820,106 555,106" fill="var(--orange-light)"/>
    <polygon points="377,60 388,60 421,106 410,106" fill="var(--navy)"/>
    <polygon points="715,106 820,106 820,122 730,122" fill="var(--navy)"/>
    <!-- watermark rule -->
    <line x1="90" y1="627" x2="640" y2="627" stroke="#fdeee4" stroke-width="2"/>
    <!-- footer -->
    <polygon points="503,1040 780,1040 794,1068 516,1068" fill="var(--orange)"/>
    <polygon points="780,1040 820,1040 820,1068 794,1068" fill="var(--navy)"/>
    <polygon points="0,1062 100,1062 94,1076 0,1076" fill="var(--navy)"/>
    <polygon points="0,1076 702,1076 728,1126 0,1126" fill="var(--orange)"/>
    <polygon points="360,1076 702,1076 728,1126 380,1126" fill="var(--orange-light)"/>
    <polygon points="673,1076 820,1076 820,1126 700,1126" fill="var(--navy)"/>
    <polygon points="0,1126 66,1126 58,1138 0,1138" fill="var(--navy)"/>
    <polygon points="66,1126 160,1126 152,1144 58,1144" fill="var(--grey)"/>
  </svg>

  <h1 class="brand-name">Brightcoil Power</h1>
  <div class="watermark-name" aria-hidden="true">Brightcoil Power</div>

  <div class="info licence">Lic. No 48162</div>
  <div class="info website">
    <svg viewBox="0 0 16 16" fill="none" stroke="#fff" stroke-width="1.3"><circle cx="8" cy="8" r="6.5"/><ellipse cx="8" cy="8" rx="3" ry="6.5"/><line x1="1.5" y1="8" x2="14.5" y2="8"/></svg>
    www.brightcoilpower.com.au
  </div>

  <div class="info email">
    <svg viewBox="0 0 16 16" fill="none" stroke="#fff" stroke-width="1.3"><rect x="1.5" y="3.5" width="13" height="9"/><polyline points="1.5,3.5 8,9 14.5,3.5"/></svg>
    info@brightcoilpower.com.au
  </div>
  <div class="info address">
    <svg viewBox="0 0 16 16" fill="#fff"><path d="M8 1a5 5 0 0 0-5 5c0 3.8 5 9 5 9s5-5.2 5-9a5 5 0 0 0-5-5zm0 7a2 2 0 1 1 0-4 2 2 0 0 1 0 4z"/></svg>
    8/22-24 Larkin Rd, Tolvern 2087
  </div>
  <div class="info phone">
    <svg viewBox="0 0 16 16" fill="none" stroke="#fff" stroke-width="1.3"><circle cx="8" cy="8" r="7"/><path d="M5.5 4.5l1.3 1.8-.8 1c.6 1.2 1.4 2 2.6 2.6l1-.8 1.8 1.3-.9 1.2C7.8 11.3 4.7 8.2 4.4 5.4z" fill="#fff" stroke="none"/></svg>
    (02) 9471 3825
  </div>
  <div class="info mobile">
    <svg viewBox="0 0 16 16" fill="none" stroke="#fff" stroke-width="1.3"><rect x="4.5" y="1.5" width="7" height="13" rx="1"/><line x1="7" y1="12" x2="9" y2="12"/></svg>
    0427 593 168
  </div>
  <div class="info abn">ABN: 42 597 214 630</div>
</main>
</body>
</html>
```